Brake Test Training for Coal Mining

We offer Brake Test Training for Coal Mine workers. It's a legislative requirement that workers who are tasked with performing brake testing have certain competencies to do so. We test Light Vehicles and trailers, Heavy Vehicles and Mobile Mining Equipment like Graders, Scrapers and Dump Trucks.

```html
<!DOCTYPE html>
<html lang="en">
<head>
<meta charset="UTF-8">
<title>Brake Test Training Billboard</title>
<link href="https://fonts.googleapis.com/css2?family=Bebas+Neue&family=Oswald:wght@300;400;600&display=swap" rel="stylesheet">
<style>
  :root {
    --navy: #0f2236;
    --navy-deep: #0b1a2b;
    --gold: #f7b718;
    --white: #ffffff;
    --silver-light: #f2f3f5;
    --silver-dark: #8d9298;
    --page: #cfcfcf;
  }
  * { margin: 0; padding: 0; box-sizing: border-box; }
  html, body {
    width: 984px; height: 1200px; overflow: hidden;
    background: var(--page);
  }
  .billboard {
    position: absolute; left: 20px; top: 364px;
    width: 944px; height: 472px;
    background: linear-gradient(135deg, var(--navy) 0%, var(--navy-deep) 100%);
    overflow: hidden;
    font-family: "Oswald", sans-serif;
  }
  .photo-frame { position: absolute; left: 0; top: 0; width: 944px; height: 472px; }
  .brand-plate {
    position: absolute; left: 594px; top: 0; width: 264px; height: 63px;
    background: var(--white);
    clip-path: polygon(0 0, 100% 0, 89% 100%, 11% 100%);
    display: flex; align-items: center; justify-content: center; gap: 8px;
  }
  .brand-dot { width: 16px; height: 16px; border-radius: 50%; background: var(--gold); }
  .brand-name {
    font-family: "Oswald", sans-serif; font-weight: 600; font-size: 14px;
    color: var(--navy); letter-spacing: 0.5px; text-transform: uppercase;
    white-space: nowrap;
  }
  .headline {
    position: absolute; left: 556px; width: 330px; text-align: center;
    font-family: "Bebas Neue", sans-serif; font-weight: 400; line-height: 1;
    white-space: nowrap;
  }
  .headline--white { top: 94px; font-size: 88px; color: var(--white); letter-spacing: -1.5px; }
  .headline--gold { top: 170px; font-size: 86px; color: var(--gold); letter-spacing: -1.5px; }
  .vehicle-list {
    position: absolute; right: 206px; top: 263px; list-style: none; text-align: right;
    font-family: "Oswald", sans-serif; font-weight: 300; color: var(--white);
    font-size: 15px; line-height: 25.5px; letter-spacing: -0.4px;
    text-transform: uppercase; white-space: nowrap;
  }
  .vehicle-list li::after {
    content: ""; display: inline-block; width: 6px; height: 6px; border-radius: 50%;
    background: var(--white); margin-left: 6px; vertical-align: middle;
  }
  .equipment-types {
    position: absolute; left: 564px; width: 180px; top: 342px; text-align: center;
    font-family: "Oswald", sans-serif; font-weight: 300; font-size: 9px;
    color: var(--gold); letter-spacing: 0.2px; white-space: nowrap;
  }
  .equipment-types span { margin: 0 3px; }
  .ute-photo {
    position: absolute; left: 749px; top: 263px; width: 160px; height: 94px;
    background: linear-gradient(160deg, #f4f5f6 0%, #d9dcdf 55%, #a9adb2 100%);
    border-radius: 6px;
  }
  .call-pill {
    position: absolute; left: 576px; top: 367px; height: 18px; width: 80px;
    display: flex; align-items: center;
  }
  .call-pill .icon {
    width: 18px; height: 18px; border-radius: 50%; background: var(--white);
    display: flex; align-items: center; justify-content: center; position: relative; z-index: 1;
  }
  .call-pill .label {
    margin-left: -6px; padding: 0 8px 0 10px; height: 13px; line-height: 13px;
    background: var(--white); color: var(--navy); border-radius: 7px;
    font-family: "Oswald", sans-serif; font-size: 9px; font-weight: 400; white-space: nowrap;
  }
  .phone-number {
    position: absolute; left: 558px; width: 330px; top: 390px; text-align: center;
    font-family: "Bebas Neue", sans-serif; font-size: 68px; line-height: 1;
    color: var(--white); letter-spacing: -0.5px; white-space: nowrap;
  }
</style>
</head>
<body>
  <section class="billboard">
    <svg class="photo-frame" viewBox="0 0 944 472">
      <defs>
        <linearGradient id="silver" x1="0" y1="0" x2="1" y2="1">
          <stop offset="0" stop-color="#8d9298"/>
          <stop offset="0.5" stop-color="#f2f3f5"/>
          <stop offset="1" stop-color="#8d9298"/>
        </linearGradient>
        <linearGradient id="quarry" x1="0" y1="0" x2="0" y2="1">
          <stop offset="0" stop-color="#c9b7ad"/>
          <stop offset="0.45" stop-color="#b59c7e"/>
          <stop offset="0.7" stop-color="#c7a338"/>
          <stop offset="1" stop-color="#cfc6b8"/>
        </linearGradient>
        <linearGradient id="truck" x1="0" y1="0" x2="0" y2="1">
          <stop offset="0" stop-color="#b8b9b8"/>
          <stop offset="0.5" stop-color="#c2a13c"/>
          <stop offset="1" stop-color="#8b8378"/>
        </linearGradient>
      </defs>
      <polygon points="0,58 432,58 533,234 432,414 0,414" fill="url(#silver)"/>
      <polygon role="img" aria-label="Photo of a large yellow wheel loader filling a mining haul truck in a rock quarry"
        points="0,67 426,67 522,234 426,405 0,405" fill="url(#quarry)"/>
      <polygon points="448,274 521,274 557,343 521,412 448,412 412,343" fill="url(#silver)"/>
      <polygon role="img" aria-label="Photo of a yellow mining dump truck"
        points="452,281 517,281 550,343 517,405 452,405 419,343" fill="url(#truck)"/>
    </svg>

    <div class="brand-plate">
      <span class="brand-dot"></span>
      <span class="brand-name">Ridgeline Operator Training</span>
    </div>

    <h1 class="headline headline--white">Brake Test</h1>
    <h2 class="headline headline--gold">Training</h2>

    <ul class="vehicle-list">
      <li>Heavy Vehicles</li>
      <li>Light Vehicles and Trailers</li>
      <li>Mobile Mining Equipment</li>
    </ul>
    <p class="equipment-types">GRADERS<span>|</span>SCRAPERS<span>|</span>DUMP TRUCKS</p>

    <div class="ute-photo" role="img" aria-label="Photo of a white service ute with a tray and a red crane"></div>

    <div class="call-pill">
      <span class="icon">
        <svg width="11" height="11" viewBox="0 0 24 24"><path fill="#0f2236" d="M6.6 10.8a15.1 15.1 0 0 0 6.6 6.6l2.2-2.2a1 1 0 0 1 1-.25 11.4 11.4 0 0 0 3.6.57 1 1 0 0 1 1 1V20a1 1 0 0 1-1 1A17 17 0 0 1 3 4a1 1 0 0 1 1-1h3.5a1 1 0 0 1 1 1c0 1.25.2 2.45.57 3.57a1 1 0 0 1-.25 1z"/></svg>
      </span>
      <span class="label">CALL US NOW</span>
    </div>
    <p class="phone-number">013 5792 4680</p>
  </section>
</body>
</html>
```